Modern design for a Septic Tank maintenance company

Task Description
- The design should be based around the attached HPID (home page information design) called Koru Flow Septic Services HPID. The table boxes are just for approximate placement of information – you DON'T have to make it look exactly like this.
- Information only is in orange text. Copy to go on the design in black text. Some instructions are in the HPID. Please be creative! You don’t have to use the exact images provided if you have a better idea.

- The design needs to be clean and spacious. Please use the colours from the logos in the website design. LOTS of white too. Don't need to use all the images attached some are customer supplied and might only be good for the smaller images.

I've attached home page gallery example photo called Tarewa beach. You can use this or something similar - be creative please!

Width of content will be 1100 pixels when implemented as a web page. Header height (without nav bar) 150-160 pixels.

The winning PSD file will have to be provided as follows…
1. Canvas size of 2000px x 2000px - 72ppi in Adobe Photoshop (CS5 compatible)
2. Width of content section is 1100px wide - centered in the canvas
3. Any button rollovers/hovers in the PSD as hidden layers.
4. All fonts used must be Google fonts (except for the fonts in the header at the top of the page).
5. You will need to supply the chosen home page plus one example page (example page as a style guide for how all other pages will look). Example page is only the header and navigational bar at the top, an empty sector in the middle with a column (180 px wide) which can be left or right aligned which means the main sector is 920 pixels wide, and then the footer at the bottom of the page.

Industry/Entity Type

It Company

```html
<!DOCTYPE html>
<html lang="en">
<head>
<meta charset="utf-8">
<title>Koru Flow Septic Services</title>
<link rel="stylesheet" href="https://fonts.googleapis.com/css2?family=Ubuntu:wght@400;500&family=Raleway:wght@500;600&family=Open+Sans:wght@400&family=Source+Sans+3:wght@400;600&display=swap">
<style>
:root{
  --teal:#12b894;
  --teal-dark:#0ea482;
  --teal-light:#6fe8cb;
  --teal-text:#16b58f;
  --ink:#222;
  --ink-soft:#333;
  --paper:#fff;
  --mist:#f3f3f3;
  --field:#efefef;
  --field-line:#9a9a9a;
  --footer:#2b2b2b;
  --footer-base:#1f1f1f;
  --footer-text:#cfcfcf;
  --button:#444;
}
*{margin:0;padding:0;box-sizing:border-box}
html,body{width:1048px;height:1200px;overflow:hidden;background:var(--paper)}
body{position:relative;font-family:"Ubuntu",sans-serif;color:var(--ink)}
.abs{position:absolute}

/* header */
.brand{left:82px;top:28px;display:flex;align-items:center;gap:12px}
.brand-dot{width:40px;height:40px;border-radius:50%;background:var(--teal)}
.brand-name{font-family:"Ubuntu",sans-serif;font-size:23px;font-weight:500;color:var(--ink)}
.tagline{left:436px;top:26px;width:210px;font-family:"Source Sans 3",sans-serif;font-size:12.5px;line-height:16px;color:var(--ink-soft)}
.contact{right:82px;top:27px;text-align:right;font-family:"Source Sans 3",sans-serif;font-weight:600;font-size:12.5px;line-height:16.5px;color:var(--ink)}
.contact .accent{color:var(--teal-text)}

/* nav */
.nav{left:80px;top:103px;width:887px;height:44px;background:var(--teal);border-radius:8px 8px 0 0;display:flex;align-items:center;justify-content:space-between;padding:0 0 0 6px}
.nav a{flex:0 0 auto;white-space:nowrap;color:#fff;text-decoration:none;font-family:"Source Sans 3",sans-serif;font-size:12.5px;font-weight:600;text-transform:uppercase;padding:0 21px;border-left:1px solid rgba(255,255,255,.25);line-height:22px}
.nav a:first-child{border-left:none}

/* feature band */
.band{left:0;top:403px;width:1048px;height:340px;background:linear-gradient(90deg,var(--teal-dark),#15c3a0 50%,var(--teal-dark))}
.hero{left:80px;top:147px;width:887px;height:302px;background:linear-gradient(180deg,#3d5a2e 0%,#8fa9b8 30%,#dfe8ee 55%,#6e8c4a 78%,#3f6d24 100%);border-bottom:2px solid #222}
.hero-caption{left:80px;top:403px;width:887px;height:44px;background:rgba(240,240,240,.88);display:flex;align-items:center;padding-left:15px}
.hero-caption p{font-family:"Open Sans",sans-serif;font-size:21px;color:#1c1c1c}
.dots{right:95px;top:419px;display:flex;gap:11px}
.dots span{width:14px;height:14px;border-radius:50%;background:#3c3c3c}
.dots span.on{background:var(--teal)}

.feature{top:467px;width:262px;color:#fff}
.feature h2{font-size:17.5px;font-weight:500;line-height:24px;height:66px;width:245px}
.feature .thumb{width:250px;height:95px;border:3px solid var(--teal-light)}
.feature p{font-family:"Source Sans 3",sans-serif;font-weight:600;font-size:12.5px;line-height:16px;margin-top:12px;width:258px}
.f1{left:88px}.f2{left:398px}.f3{left:711px}
.f2 p{padding-left:5px}
.t1{background:linear-gradient(180deg,#5b4a2c,#8a7651 55%,#4c6a2c)}
.t2{background:linear-gradient(180deg,#1f3a55,#c9d9e6 45%,#3d7a3a)}
.t3{background:linear-gradient(180deg,#7aa7c9,#2e7ea0 45%,#5f5a48 75%,#b9b3a3)}

/* enquiry */
.enquiry{left:0;top:743px;width:1048px;height:223px;background:var(--mist)}
.enquiry-title{left:108px;top:803px;font-family:"Raleway",sans-serif;font-weight:600;font-size:33px;color:#222}
.enquiry-lead{left:109px;top:851px;width:250px;font-family:"Source Sans 3",sans-serif;font-size:14.5px;line-height:16px;color:#222}
.field{width:222px;height:29px;background:var(--field);border:1px solid var(--field-line);font-family:"Source Sans 3",sans-serif;font-size:12px;color:#333;padding:6px 8px}
.field-name{left:421px;top:800px}
.field-email{left:421px;top:841px}
.field-phone{left:421px;top:883px}
.field-details{left:699px;top:800px;height:77px}
.send{left:808px;top:897px;width:111px;height:31px;background:var(--button);border-radius:3px;color:#fff;font-family:"Open Sans",sans-serif;font-size:18px;display:flex;align-items:center;justify-content:center;box-shadow:0 1px 2px rgba(0,0,0,.4)}

/* footer */
.footer{left:0;top:966px;width:1048px;height:205px;background:var(--footer)}
.footer-base{left:0;top:1171px;width:1048px;height:29px;background:var(--footer-base);color:#bbb;font-family:Arial,sans-serif;font-size:11px;display:flex;align-items:center;justify-content:center}
.footer h3{font-family:"Raleway",sans-serif;font-weight:500;font-size:16px;line-height:19px;color:#fff}
.footer-text{font-family:"Source Sans 3",sans-serif;font-size:12px;line-height:14.5px;color:var(--footer-text)}
.divider{top:997px;width:1px;height:152px;background:#4a4a4a}
.nav-col{font-family:"Source Sans 3",sans-serif;font-size:14px;color:var(--footer-text);line-height:29px}
</style>
</head>
<body>

<header>
  <div class="abs brand"><span class="brand-dot"></span><span class="brand-name">Koru Flow Septic Services</span></div>
  <p class="abs tagline">Our Septic tank maintenance services will help your septic system perform at optimum efficiency</p>
  <p class="abs contact">For Septic Tank servicing, installation and<br><span class="accent">parts Auckland Wide</span><br>09 555 0142 , 021 555 01 234</p>
</header>

<div class="abs band"></div>
<nav class="abs nav">
  <a>Home</a><a>About Us</a><a>Deciphering Your Septic Tank</a><a>Servicing &amp; Maintenance</a><a>Parts</a><a>Free Quote</a><a>Contact Us</a>
</nav>

<div class="abs hero" role="img" aria-label="Wide waterfall cascading over mossy rock into a bush pool"></div>
<div class="abs hero-caption"><p>Koru Flow Septic Services are Auckland best septic tank experts.</p></div>
<div class="abs dots"><span></span><span class="on"></span><span></span></div>

<section class="abs feature f1">
  <h2>Looking for septic tanks parts in Auckland asap?</h2>
  <div class="thumb t1" role="img" aria-label="Septic tank lids set into the ground"></div>
  <p>If you need replacement parts for septic tanks, call us today! Koru Flow Septic Services will either have or can source the part you need fast and offer septic tank part installation</p>
</section>
<section class="abs feature f2">
  <h2>Want to know how to take care of your septic tank?</h2>
  <div class="thumb t2" role="img" aria-label="Waterfall above green forest"></div>
  <p>Most people when they buy a new property with a septic tank don't understand how their system works, or even what system they have! Koru Flow Septic Services.</p>
</section>
<section class="abs feature f3">
  <h2>When was the last time you serviced your septic tank?</h2>
  <div class="thumb t3" role="img" aria-label="Tarewa beach coastline with a rock headland"></div>
  <p>Standard septic tanks need to be serviced every 3 - 5 years and as each septic system has its own unique characteristics, such as internal parts and control panels.</p>
</section>

<section class="abs enquiry"></section>
<h2 class="abs enquiry-title">Make An Enquiry</h2>
<p class="abs enquiry-lead">Fill out the form below and we will contact you within 24hrs.</p>
<div class="abs field field-name">Name: *</div>
<div class="abs field field-email">Email: *</div>
<div class="abs field field-phone">Contact phone: *</div>
<div class="abs field field-details">Details:</div>
<div class="abs send">Send</div>

<footer class="abs footer"></footer>
<h3 class="abs" style="left:79px;top:993px;font-family:'Raleway',sans-serif;font-weight:500;font-size:16px;color:#fff">Navigation</h3>
<div class="abs nav-col" style="left:81px;top:1023px">Home<br>About<br>Deciphering Your Septic tank<br>Servicing &amp; Maintenance</div>
<div class="abs nav-col" style="left:273px;top:1023px">Parts<br>Free Quote<br>Contact</div>
<div class="abs divider" style="left:368px"></div>
<div class="abs footer" style="left:396px;top:994px;width:292px;height:160px;background:none">
  <h3>Company guarantee to you...</h3>
  <p class="footer-text" style="margin-top:13px">Koru Flow Septic Services travel throughout the Auckland region. Owner Rangi promises they will go through your comb a comprehensive service.</p>
  <p class="footer-text" style="margin-top:14px">Koru Flow Septic Services aim to give clients more than they expect from their septic tank service.</p>
  <p class="footer-text" style="margin-top:14px">And most we sell come with a one year guarantee.</p>
</div>
<div class="abs divider" style="left:717px"></div>
<div class="abs footer" style="left:749px;top:991px;width:220px;height:160px;background:none">
  <h3>Need your septic tank cleaned?</h3>
  <p class="footer-text" style="margin-top:8px">Talk to the team at Harbourside Tank Cleaning Services!</p>
  <h3 style="margin-top:12px">For all polymer fabricated products</h3>
  <p class="footer-text" style="margin-top:9px">Talk to the team at Northfab 09 Limited!</p>
</div>
<div class="abs footer-base">© Copyright&nbsp; Koru Flow.&nbsp; All Rights Reserved</div>

</body>
</html>
```